Redesign of business card for Birchline Mechanical

We are looking for a new design for our business cards for Birchline Mechanical. We are a plumbing & HVAC construction company, operating on the West Coast of Canada and USA. Logo attached.
Industry/Entity Type
Construction - Plumbing & HVAC
Contact Information for Business Card
Name, address, phone numbers, email, website address
Look and feel
Each slider illustrates characteristics of the customer's brand and the style your logo design should communicate.

```html
<!DOCTYPE html>
<html lang="en">
<head>
<meta charset="utf-8">
<title>Birchline Mechanical – Business Card</title>
<link href="https://fonts.googleapis.com/css2?family=Jost:wght@400&family=Oswald:wght@500&display=swap" rel="stylesheet">
<style>
  :root {
    --backdrop: #777777;
    --paper: #ffffff;
    --ink: #000000;
    --shadow: rgba(0, 0, 0, 0.35);
  }
  html, body {
    margin: 0;
    padding: 0;
    width: 1200px;
    height: 1200px;
    overflow: hidden;
    background: var(--backdrop);
  }
  .canvas {
    position: relative;
    width: 1200px;
    height: 1200px;
  }
  .card {
    position: absolute;
    left: 150px;
    width: 898px;
    height: 525px;
    box-shadow: 0 4px 14px var(--shadow);
  }
  .card--front { top: 55px; background: var(--paper); color: var(--ink); }
  .card--back { top: 621px; background: var(--ink); color: var(--paper); }

  .brand-name {
    position: absolute;
    display: flex;
    align-items: center;
    gap: 14px;
    font-family: "Oswald", sans-serif;
    font-weight: 500;
    text-transform: uppercase;
    letter-spacing: 0.03em;
    white-space: nowrap;
  }
  .brand-name__mark {
    flex: none;
    background: currentColor;
  }
  .card--front .brand-name {
    right: 75px;
    top: 168px;
    font-size: 38px;
    line-height: 1;
  }
  .card--front .brand-name__mark { width: 26px; height: 26px; }
  .card--back .brand-name {
    left: 0;
    right: 0;
    top: 222px;
    justify-content: center;
    font-size: 64px;
    line-height: 1;
  }
  .card--back .brand-name__mark { width: 42px; height: 42px; }

  .contact-list {
    position: absolute;
    left: 56px;
    top: 265px;
    margin: 0;
    padding: 0;
    list-style: none;
    font-family: "Jost", sans-serif;
    font-size: 22px;
    line-height: 1;
  }
  .contact-list__item {
    display: flex;
    align-items: center;
    height: 36px;
    margin-bottom: 6px;
  }
  .contact-list__item--address { margin-top: 26px; }
  .contact-list__icon {
    width: 20px;
    height: 20px;
    margin-right: 30px;
    flex: none;
  }
</style>
</head>
<body>
<main class="canvas">
  <section class="card card--front">
    <div class="brand-name"><span class="brand-name__mark"></span>Birchline Mechanical</div>
    <ul class="contact-list">
      <li class="contact-list__item">
        <svg class="contact-list__icon" viewBox="0 0 24 24" aria-hidden="true"><path fill="currentColor" d="M6.6 10.8a15.1 15.1 0 0 0 6.6 6.6l2.2-2.2a1 1 0 0 1 1-.25 11.4 11.4 0 0 0 3.6.57 1 1 0 0 1 1 1V20a1 1 0 0 1-1 1A17 17 0 0 1 3 4a1 1 0 0 1 1-1h3.5a1 1 0 0 1 1 1c0 1.25.2 2.45.57 3.57a1 1 0 0 1-.25 1z"/></svg>
        <span>1234 567 890</span>
      </li>
      <li class="contact-list__item">
        <svg class="contact-list__icon" viewBox="0 0 24 24" aria-hidden="true"><path fill="currentColor" d="M3 5h18a1 1 0 0 1 1 1v12a1 1 0 0 1-1 1H3a1 1 0 0 1-1-1V6a1 1 0 0 1 1-1zm9 7.5L20 7.5V7H4v.5z"/></svg>
        <span>info@birchlinemech.com</span>
      </li>
      <li class="contact-list__item">
        <svg class="contact-list__icon" viewBox="0 0 24 24" aria-hidden="true"><g fill="none" stroke="currentColor" stroke-width="2"><circle cx="12" cy="12" r="9"/><ellipse cx="12" cy="12" rx="4" ry="9"/><path d="M3 12h18M5 7h14M5 17h14"/></g></svg>
        <span>www.birchlinemech.com</span>
      </li>
      <li class="contact-list__item contact-list__item--address">
        <svg class="contact-list__icon" viewBox="0 0 24 24" aria-hidden="true"><path fill="currentColor" d="M12 2a7 7 0 0 0-7 7c0 5 7 13 7 13s7-8 7-13a7 7 0 0 0-7-7zm0 9.5A2.5 2.5 0 1 1 12 6.5a2.5 2.5 0 0 1 0 5z"/></svg>
        <span>12/C, Address, Street, Pincode - 221122</span>
      </li>
    </ul>
  </section>

  <section class="card card--back">
    <div class="brand-name"><span class="brand-name__mark"></span>Birchline Mechanical</div>
  </section>
</main>
</body>
</html>
```